Net Clarity Partners Needs a New Business Card Design

Attached is my new logo that ArtFlockly created and picture of me for the back of the business card. Also attached is the information to include on the business card (on my existing business card design - NCP1 file attached).

The designer also provided a treatment of my logo that I really like if you can use it somehow. Also attached - file name "Preferred Version of New Logo."

Marla Quinteros

Net Clarity Partners
4817 Brindle Ave., #315
Houston, TX 77056

Tel: (832) 555-0147
www.netclaritypartners.example
marla@netclaritypartners.example

Thank you.

Target Market(s)

attorneys and law firms

Industry/Entity Type

Legal

Contact Information for Business Card

Proved in the Project Description

Font styles to use
Other font styles liked:
• I am open on font - no script though.

Colors
2d73b3
33a6d7

Requirements
Must have
• my logo
• company name & contact info
• my picture on the back
• colors that coordinate with the logo
Nice to have
• love to use the treated version of the logo if possible

```html
<!DOCTYPE html>
<html lang="en">
<head>
<meta charset="utf-8">
<title>Net Clarity Partners — Business Card</title>
<link rel="stylesheet" href="https://fonts.googleapis.com/css2?family=Open+Sans:wght@400;600;700&display=swap">
<style>
  :root {
    --stage: #e9ebee;
    --card-white: #ffffff;
    --brand-blue: #2ba3dc;
    --brand-deep: #2d73b3;
    --text-gray: #6b6e72;
    --rule-gray: #9a9da1;
    --band-gray: #9c9ea2;
    --back-dark: #1e2936;
    --back-mid: #3b4a5b;
    --back-light: #5f6f80;
    --back-name: #8fc3e6;
    --photo-tone: #8c8f96;
  }
  * { box-sizing: border-box; margin: 0; padding: 0; }
  html, body {
    width: 1200px; height: 1000px; overflow: hidden;
    background: var(--stage);
    font-family: "Open Sans", Arial, sans-serif;
  }
  .canvas { position: relative; width: 1200px; height: 1000px; }

  .card {
    position: absolute; left: 266px; width: 666px; height: 397px;
    box-shadow: 0 6px 16px rgba(0,0,0,0.25);
    overflow: hidden;
  }
  .card--front { top: 74px; background: var(--card-white); }
  .card--back { top: 533px; }

  .brand-name {
    position: absolute; left: 32px; top: 130px;
    font-size: 23px; font-weight: 700; letter-spacing: 0.5px;
    text-transform: uppercase; color: var(--brand-blue);
  }

  .portrait {
    position: absolute; left: 488px; top: 51px;
    width: 146px; height: 146px; border-radius: 50%;
    border: 3px solid var(--brand-blue);
    background: radial-gradient(circle at 50% 40%, #a9a3a0 0%, var(--photo-tone) 55%, #4b5fa8 100%);
  }

  .person {
    position: absolute; right: 33px; top: 205px; text-align: right;
  }
  .person__name { font-size: 24px; font-weight: 600; color: var(--brand-blue); line-height: 1.2; }
  .person__title { font-size: 16px; color: var(--text-gray); line-height: 1.2; }

  .divider {
    position: absolute; left: 32px; top: 244px;
    width: 450px; height: 2px; background: var(--rule-gray);
  }

  .contact { position: absolute; left: 32px; top: 274px; list-style: none; }
  .contact__item {
    display: flex; align-items: center; gap: 8px;
    font-size: 16px; color: var(--text-gray); height: 24px;
  }
  .contact__icon { width: 15px; height: 15px; fill: var(--brand-deep); }

  .address {
    position: absolute; right: 33px; top: 297px; text-align: right;
    font-size: 16px; color: var(--text-gray); line-height: 23px;
  }

  .band { position: absolute; left: 0; bottom: 0; width: 666px; height: 26px; }

  .back-scene {
    position: absolute; inset: 0;
    background: linear-gradient(115deg, var(--back-dark) 0%, var(--back-mid) 55%, var(--back-light) 100%);
  }
  .back-brand {
    position: absolute; left: 0; right: 0; top: 200px; text-align: center;
    font-size: 32px; font-weight: 700; letter-spacing: 1px;
    text-transform: uppercase; color: var(--back-name);
  }
</style>
</head>
<body>
<main class="canvas">

  <section class="card card--front" aria-label="Business card front">
    <div class="brand-name">Net Clarity Partners</div>

    <div class="portrait" role="img" aria-label="Portrait photo of Marla Quinteros"></div>

    <div class="person">
      <div class="person__name">Marla Quinteros</div>
      <div class="person__title">Managing Director</div>
    </div>

    <div class="divider"></div>

    <ul class="contact">
      <li class="contact__item">
        <svg class="contact__icon" viewBox="0 0 16 16" aria-hidden="true"><path d="M3 2h3l1.5 3.5-2 1.2a8 8 0 0 0 3.8 3.8l1.2-2L14 10v3a1 1 0 0 1-1 1A11 11 0 0 1 2 3a1 1 0 0 1 1-1z"/></svg>
        (832) 555-0147
      </li>
      <li class="contact__item">
        <svg class="contact__icon" viewBox="0 0 16 16" aria-hidden="true"><path d="M1 3h14v10H1z M2 4l6 5 6-5" fill="none" stroke="var(--brand-deep)" stroke-width="1.6"/></svg>
        marla@netclaritypartners.example
      </li>
      <li class="contact__item">
        <svg class="contact__icon" viewBox="0 0 16 16" aria-hidden="true"><g fill="none" stroke="var(--brand-deep)" stroke-width="1.4"><circle cx="8" cy="8" r="6.5"/><ellipse cx="8" cy="8" rx="2.8" ry="6.5"/><path d="M1.5 8h13"/></g></svg>
        www.netclaritypartners.example
      </li>
    </ul>

    <div class="address">
      4817 Brindle Ave., #315<br>
      Houston, TX 77056
    </div>

    <svg class="band" viewBox="0 0 666 26" aria-hidden="true">
      <polygon points="0,2 340,2 364,26 0,26" fill="var(--brand-blue)"/>
      <polygon points="346,2 666,2 666,26 370,26" fill="var(--band-gray)"/>
    </svg>
  </section>

  <section class="card card--back" aria-label="Business card back">
    <div class="back-scene" role="img" aria-label="Dim office interior photograph in dark blue-gray tones"></div>
    <div class="back-brand">Net Clarity Partners</div>
  </section>

</main>
</body>
</html>
```